Tidal Ledger

Please see attached Word document for requirements. I want the website to be one page.

Coding

Coded - Northfield and coding required

Number of Pages Required

1 page

Colors
0054AA
0677BA
7BADD7
CADEEF
E8F1F8

```html
<!DOCTYPE html>
<html lang="en">
<head>
<meta charset="utf-8">
<title>Tidal Ledger – Smarter Scheduling</title>
<link href="https://fonts.googleapis.com/css2?family=Inter:wght@400;500;600;700;800&display=swap" rel="stylesheet">
<style>
:root{
  --blue-900:#0a2f8c;
  --blue-800:#0f3fa6;
  --blue:#0054AA;
  --blue-mid:#0677BA;
  --blue-soft:#7BADD7;
  --blue-pale:#CADEEF;
  --blue-mist:#E8F1F8;
  --ink:#111827;
  --text:#374151;
  --muted:#6b7280;
  --white:#ffffff;
  --star:#f59e0b;
}
*{box-sizing:border-box;margin:0;padding:0}
html,body{width:1200px;height:4464px;overflow:hidden}
body{font-family:"Inter",sans-serif;color:var(--text);background:var(--white);position:relative}
.section{position:absolute;left:0;width:1200px}
h2.section-title{font-size:44px;font-weight:700;color:var(--ink);text-align:center;letter-spacing:-.5px}
.title-rule{width:48px;height:4px;border-radius:2px;background:var(--blue);margin:14px auto 0}
.btn{display:inline-flex;align-items:center;justify-content:center;height:34px;padding:0 22px;border-radius:17px;font-size:13px;font-weight:600;text-decoration:none}
.btn-solid{background:var(--blue);color:var(--white)}
.btn-outline{background:var(--white);color:var(--blue);border:1.5px solid var(--blue)}

/* header + hero */
.hero{top:0;height:520px;background:linear-gradient(160deg,var(--blue-mist) 0%,#f4f8fc 45%,var(--blue-pale) 100%);overflow:hidden}
.hero-wave{position:absolute;left:0;top:0}
.nav{position:absolute;top:0;left:0;width:1200px;height:72px;display:flex;align-items:center;padding:0 144px}
.brand{font-size:22px;font-weight:700;color:var(--blue-800);display:flex;align-items:center;gap:8px}
.brand-dot{width:10px;height:10px;border-radius:50%;background:var(--blue-soft)}
.nav-links{display:flex;gap:26px;margin-left:auto;margin-right:64px;list-style:none;position:relative;left:-60px}
.nav-links a{font-size:14px;font-weight:500;color:var(--ink);text-decoration:none}
.nav-links .active{color:var(--blue);border-bottom:2px solid var(--blue);padding-bottom:4px}
.btn-signin{height:32px;padding:0 20px;font-size:13px}
.hero-copy{position:absolute;left:144px;top:156px;width:440px}
.hero-copy h1{font-size:50px;line-height:56px;font-weight:800;color:var(--ink);letter-spacing:-1px}
.hero-copy p{margin-top:16px;font-size:15px;line-height:22px;color:var(--text)}
.hero-actions{margin-top:22px;display:flex;gap:12px}
.hero-visual{position:absolute;left:640px;top:86px;width:440px;height:320px;border-radius:14px;background:linear-gradient(135deg,#dbe9f6,var(--blue-soft) 60%,var(--blue-mid));box-shadow:0 20px 40px rgba(0,84,170,.18)}
.slider-dots{position:absolute;left:144px;top:486px;display:flex;gap:10px}
.slider-dots span{width:12px;height:12px;border-radius:50%;background:var(--blue-pale)}
.slider-dots span.on{background:var(--blue)}

/* values */
.values{top:620px}
.value-list{display:flex;justify-content:center;gap:40px;margin-top:56px}
.value{width:200px;text-align:center}
.value-icon{width:140px;height:140px;border-radius:50%;background:var(--blue-mist);margin:0 auto;display:flex;align-items:center;justify-content:center}
.value-icon-inner{width:108px;height:108px;border-radius:50%;background:var(--white);border:3px solid var(--blue-pale);display:flex;align-items:center;justify-content:center}
.value h3{margin-top:18px;font-size:19px;font-weight:700;color:var(--ink);line-height:24px}
.value p{margin-top:8px;font-size:14px;line-height:20px;color:var(--muted)}

/* features */
.features{top:1184px;height:420px}
.feature-row{position:relative;height:300px;margin-top:50px}
.feature{position:absolute;width:260px;height:260px;border-radius:50%;display:flex;flex-direction:column;align-items:center;justify-content:center;text-align:center;color:var(--white);font-size:15px;font-weight:600;line-height:20px;gap:14px}
.feature.up{top:0;background:linear-gradient(160deg,var(--blue-soft),var(--blue-mid));box-shadow:0 10px 26px rgba(0,84,170,.25)}
.feature.down{top:50px;background:linear-gradient(160deg,var(--blue-mid),var(--blue-900));z-index:2;box-shadow:0 10px 26px rgba(10,47,140,.35)}
.feature-badge{width:54px;height:54px;border-radius:50%;border:2px solid rgba(255,255,255,.8);display:flex;align-items:center;justify-content:center}

/* industries */
.industries{top:1716px}
.industry-row{display:flex;justify-content:center;gap:20px;margin-top:50px}
.industry{width:216px;text-align:center}
.industry-photo{height:280px;border-radius:12px}
.industry h3{margin-top:22px;font-size:17px;font-weight:600;color:var(--ink)}
.industry h3.current{color:var(--blue);text-decoration:underline;text-underline-offset:4px}
.bar-dots{display:flex;justify-content:center;gap:8px;margin-top:34px}
.bar-dots span{width:40px;height:4px;border-radius:2px;background:var(--blue-pale)}
.bar-dots span.on{background:var(--blue)}

/* testimonials */
.testimonials{top:2320px;height:500px;background:linear-gradient(180deg,var(--blue-mist),#f6f9fd 60%,var(--blue-mist));padding-top:128px}
.quote-row{position:relative;display:flex;justify-content:center;align-items:flex-start;gap:36px;margin-top:44px}
.quote{width:256px;background:var(--white);border-radius:12px;box-shadow:0 8px 24px rgba(0,84,170,.12);padding:22px 22px 26px;text-align:center}
.quote.feature-quote{width:280px;border-bottom:4px solid var(--blue)}
.client{font-size:22px;font-weight:700;color:var(--ink);display:flex;align-items:center;justify-content:center;gap:8px;height:34px}
.client-mark{width:14px;height:14px;border-radius:3px;background:var(--blue-mid)}
.stars{color:var(--star);font-size:15px;letter-spacing:2px;margin-top:6px}
.quote p{margin-top:8px;font-size:13px;line-height:19px;font-style:italic;color:var(--text)}
.arrow{position:absolute;top:80px;width:32px;height:32px;border-radius:50%;background:var(--blue);display:flex;align-items:center;justify-content:center}

/* pricing */
.pricing{top:3020px}
.plan-row{display:flex;justify-content:center;align-items:flex-start;gap:32px;margin-top:50px}
.plan{width:284px;height:392px;margin-top:28px;border-radius:12px;background:var(--white);box-shadow:0 6px 20px rgba(0,0,0,.08);text-align:center;overflow:hidden;position:relative}
.plan-head{padding-top:22px}
.plan-name{font-size:17px;font-weight:700;color:var(--ink);letter-spacing:.5px}
.plan-sub{font-size:13px;color:var(--muted);margin-top:4px}
.price{margin:14px 0 0;height:56px;display:flex;align-items:center;justify-content:center;background:var(--blue);color:var(--white);font-size:32px;font-weight:700}
.plan ul{list-style:none;text-align:left;padding:20px 28px 0;font-size:13px;line-height:32px;color:var(--text)}
.plan li{display:flex;align-items:center;gap:10px}
.tick{width:14px;height:14px;border-radius:50%;background:var(--blue-mid);flex:none}
.plan .btn{position:absolute;left:50%;transform:translateX(-50%);bottom:24px}
.plan.popular{height:440px;margin-top:0;background:linear-gradient(180deg,var(--blue-800),var(--blue))}
.plan.popular .plan-name{color:var(--white)}
.plan.popular .plan-sub{color:var(--blue-pale)}
.plan.popular .price{background:var(--blue-soft)}
.plan.popular ul{color:var(--white)}
.plan.popular .tick{background:var(--white)}
.plan.popular ul li{border-bottom:1px solid rgba(255,255,255,.2)}

/* cta */
.cta{top:3700px;height:332px;background:linear-gradient(120deg,var(--blue-900),var(--blue) 55%,var(--blue-mid));text-align:center;color:var(--white);padding-top:92px}
.cta h2{font-size:42px;font-weight:800;letter-spacing:-.5px}
.cta p{margin-top:16px;font-size:18px;font-weight:600}
.cta-actions{margin-top:26px;display:flex;justify-content:center;gap:14px}
.cta .btn-outline{background:transparent;color:var(--white);border-color:var(--white)}
.cta .btn-solid{background:var(--white);color:var(--blue)}

/* footer */
.footer{top:4140px}
.footer-cols{position:relative;height:220px}
.footer-col{position:absolute;top:0}
.footer-col h4{font-size:19px;font-weight:700;color:var(--ink);margin-bottom:14px}
.footer-col p{font-size:13px;line-height:19px;color:var(--text);width:300px}
.footer-col ul{list-style:none;font-size:13px;line-height:21px;color:var(--text)}
.footer-col li{display:flex;align-items:center;gap:8px}
.footer-col li::before{content:"";width:6px;height:6px;border-radius:50%;background:var(--blue)}
.copyright{position:absolute;top:244px;width:1200px;text-align:center;font-size:13px;color:var(--ink)}
.copyright span{position:absolute;right:40px;font-size:11px;color:var(--muted)}
</style>
</head>
<body>

<section class="section hero">
  <svg class="hero-wave" width="1200" height="520" viewBox="0 0 1200 520" aria-hidden="true">
    <path d="M0 380 C300 300 520 470 820 400 S1100 300 1200 330 L1200 520 L0 520Z" fill="#CADEEF" opacity=".55"/>
    <path d="M0 440 C260 380 560 500 860 450 S1120 400 1200 420 L1200 520 L0 520Z" fill="#ffffff" opacity=".6"/>
    <path d="M600 0 C760 120 900 60 1200 180 L1200 0Z" fill="#E8F1F8" opacity=".8"/>
  </svg>
  <nav class="nav">
    <div class="brand"><span class="brand-dot"></span>Tidal Ledger</div>
    <ul class="nav-links">
      <li><a class="active" href="#">Home</a></li>
      <li><a href="#">Features</a></li>
      <li><a href="#">Pricing</a></li>
      <li><a href="#">Contact</a></li>
    </ul>
    <a class="btn btn-solid btn-signin" href="#">Sign In</a>
  </nav>
  <div class="hero-copy">
    <h1>Smarter Scheduling.<br>Zero Stress.</h1>
    <p>Tidal Ledger automates workforce scheduling with intelligent tools that save time, reduce costs, and ensure fairness—across any industry.</p>
    <div class="hero-actions">
      <a class="btn btn-solid" href="#">Start Free Trial</a>
      <a class="btn btn-outline" href="#">Book a Demo</a>
    </div>
  </div>
  <div class="hero-visual" role="img" aria-label="Laptop showing the scheduling dashboard with cloud and analytics graphics"></div>
  <div class="slider-dots"><span class="on"></span><span></span><span></span><span></span></div>
</section>

<section class="section values">
  <h2 class="section-title">Our Values</h2>
  <div class="title-rule"></div>
  <div class="value-list">
    <div class="value">
      <div class="value-icon"><div class="value-icon-inner">
        <svg width="48" height="48" viewBox="0 0 48 48" fill="none" stroke="#0054AA" stroke-width="2.5"><rect x="8" y="10" width="32" height="22" rx="2"/><path d="M18 38h12M24 32v6M16 24l5-6 5 4 6-8"/></svg>
      </div></div>
      <h3>Intelligent by<br>Design</h3>
      <p>Advanced automation that thinks ahead, not just reacts.</p>
    </div>
    <div class="value">
      <div class="value-icon"><div class="value-icon-inner">
        <svg width="48" height="48" viewBox="0 0 48 48" fill="none" stroke="#0054AA" stroke-width="2.5"><circle cx="24" cy="24" r="8"/><path d="M24 8v6M24 34v6M8 24h6M34 24h6M13 13l4 4M31 31l4 4M35 13l-4 4M17 31l-4 4"/></svg>
      </div></div>
      <h3>Effortless<br>Control</h3>
      <p>Manage complex schedules with simple, intuitive tools.</p>
    </div>
    <div class="value">
      <div class="value-icon"><div class="value-icon-inner">
        <svg width="48" height="48" viewBox="0 0 48 48" fill="none" stroke="#0054AA" stroke-width="2.5"><circle cx="24" cy="24" r="15"/><path d="M24 14v10l7 5"/></svg>
      </div></div>
      <h3>Optimised<br>Operations</h3>
      <p>Reduce inefficiencies and maximise workforce performance.</p>
    </div>
    <div class="value">
      <div class="value-icon"><div class="value-icon-inner">
        <svg width="48" height="48" viewBox="0 0 48 48" fill="none" stroke="#0054AA" stroke-width="2.5"><rect x="8" y="10" width="32" height="28" rx="2"/><path d="M8 18h32M16 6v8M32 6v8M16 26h4M28 26h4M16 32h4"/></svg>
      </div></div>
      <h3>People-First<br>Scheduling</h3>
      <p>Fair, balanced rosters that work for everyone.</p>
    </div>
  </div>
</section>

<section class="section features">
  <h2 class="section-title">Features Overview</h2>
  <div class="title-rule"></div>
  <div class="feature-row">
    <div class="feature up" style="left:30px"><span class="feature-badge"><svg width="26" height="26" viewBox="0 0 26 26" fill="none" stroke="#fff" stroke-width="2"><rect x="4" y="5" width="18" height="17" rx="2"/><path d="M4 10h18M9 3v4M17 3v4"/></svg></span>Automated<br>Scheduling</div>
    <div class="feature down" style="left:250px"><span class="feature-badge"><svg width="26" height="26" viewBox="0 0 26 26" fill="none" stroke="#fff" stroke-width="2"><path d="M13 3l8 3v7c0 5-4 8-8 10-4-2-8-5-8-10V6z"/><path d="M9 13l3 3 5-6"/></svg></span>Compliance<br>Engine</div>
    <div class="feature up" style="left:470px"><span class="feature-badge"><svg width="26" height="26" viewBox="0 0 26 26" fill="none" stroke="#fff" stroke-width="2"><circle cx="13" cy="13" r="9"/><path d="M13 7v12M16 9.5h-4.5a2 2 0 000 4h3a2 2 0 010 4H9"/></svg></span>Cost<br>Optimisation</div>
    <div class="feature down" style="left:690px"><span class="feature-badge"><svg width="26" height="26" viewBox="0 0 26 26" fill="none" stroke="#fff" stroke-width="2"><circle cx="13" cy="13" r="9"/><path d="M4 13h18M13 4c3 3 3 15 0 18M13 4c-3 3-3 15 0 18"/></svg></span>Multi Site<br>Support</div>
    <div class="feature up" style="left:910px"><span class="feature-badge"><svg width="26" height="26" viewBox="0 0 26 26" fill="none" stroke="#fff" stroke-width="2"><circle cx="13" cy="9" r="4"/><path d="M5 22c0-4.5 3.5-7 8-7s8 2.5 8 7"/></svg></span>Staff<br>Self Service</div>
  </div>
</section>

<section class="section industries">
  <h2 class="section-title">Industries Served</h2>
  <div class="title-rule"></div>
  <div class="industry-row">
    <div class="industry"><div class="industry-photo" role="img" aria-label="Healthcare staff working at a hospital station" style="background:linear-gradient(160deg,#9fb4c8,#4d6780)"></div><h3>Healthcare</h3></div>
    <div class="industry"><div class="industry-photo" role="img" aria-label="Retail checkout with a shopping basket and card payment" style="background:linear-gradient(160deg,#2a3f7a,#0b1c45)"></div><h3 class="current">Retail</h3></div>
    <div class="industry"><div class="industry-photo" role="img" aria-label="Hotel reception team at the front desk" style="background:linear-gradient(160deg,#d8dde6,#6b7a93)"></div><h3>Hospitality</h3></div>
    <div class="industry"><div class="industry-photo" role="img" aria-label="Container port with cranes at dusk" style="background:linear-gradient(180deg,#b7a7d6,#d59bb4 55%,#6d7ea8)"></div><h3>Logistics</h3></div>
  </div>
  <div class="bar-dots"><span></span><span class="on"></span><span></span></div>
</section>

<section class="section testimonials">
  <h2 class="section-title">What Our Clients Say</h2>
  <div class="title-rule"></div>
  <div class="quote-row">
    <span class="arrow" style="left:52px"><svg width="12" height="12" viewBox="0 0 12 12"><path d="M8 1L3 6l5 5" fill="none" stroke="#fff" stroke-width="2"/></svg></span>
    <div class="quote"><div class="client"><span class="client-mark"></span>Northfield</div><div class="stars">★★★★★</div><p>Rosters used to take hours each week. Now the schedule is built in minutes and our team always knows where they need to be.</p></div>
    <div class="quote feature-quote"><div class="client">Sproutline</div><div class="stars">★★★★★</div><p>We cut overtime costs within the first month. The compliance checks give our managers real peace of mind every single day.</p></div>
    <div class="quote"><div class="client">Kestrel Works</div><div class="stars">★★★★★</div><p>Running five sites is far simpler now. Staff swap shifts on their own and every change is clear, fair and tracked.</p></div>
    <span class="arrow" style="left:1112px"><svg width="12" height="12" viewBox="0 0 12 12"><path d="M4 1l5 5-5 5" fill="none" stroke="#fff" stroke-width="2"/></svg></span>
  </div>
</section>

<section class="section pricing">
  <h2 class="section-title">Simple, Transparent Pricing</h2>
  <div class="title-rule"></div>
  <div class="plan-row">
    <div class="plan">
      <div class="plan-head"><div class="plan-name">STARTER</div><div class="plan-sub">For small teams getting started</div></div>
      <div class="price">$25.00<small style="font-size:14px;font-weight:500">/mo</small></div>
      <ul><li><span class="tick"></span>Core scheduling features</li><li><span class="tick"></span>Up to X employees</li><li><span class="tick"></span>Basic reporting</li><li><span class="tick"></span>Email support</li></ul>
      <a class="btn btn-outline" href="#">Get Started</a>
    </div>
    <div class="plan popular">
      <div class="plan-head"><div class="plan-name">PROFESSIONAL</div><div class="plan-sub">Tools for growing businesses</div></div>
      <div class="price">$50.00<small style="font-size:14px;font-weight:500">/mo</small></div>
      <ul><li><span class="tick"></span>Advanced scheduling automation</li><li><span class="tick"></span>Compliance tools</li><li><span class="tick"></span>Cost optimisation insights</li><li><span class="tick"></span>Multi-location support</li></ul>
      <a class="btn btn-outline" href="#" style="border-color:#fff">Start Free Trial</a>
    </div>
    <div class="plan">
      <div class="plan-head"><div class="plan-name">ENTERPRISE</div><div class="plan-sub">Solutions for large organisations</div></div>
      <div class="price">$75.00<small style="font-size:14px;font-weight:500">/mo</small></div>
      <ul><li><span class="tick"></span>Full platform access</li><li><span class="tick"></span>Custom integrations</li><li><span class="tick"></span>Dedicated support</li><li><span class="tick"></span>Advanced analytics</li></ul>
      <a class="btn btn-outline" href="#">Contact Sales</a>
    </div>
  </div>
</section>

<section class="section cta">
  <h2>Ready To Transform Your Workforce?</h2>
  <p>Start automating your scheduling today and experience the power of intelligent rostering.</p>
  <div class="cta-actions">
    <a class="btn btn-solid" href="#">Start Free Trial</a>
    <a class="btn btn-outline" href="#">Book a Demo</a>
  </div>
</section>

<footer class="section footer">
  <div class="footer-cols">
    <div class="footer-col" style="left:144px"><h4>Our Mission</h4><p>We help every team build fair, efficient rosters with less effort, so managers spend less time on admin and more time leading their people toward better days at work.</p></div>
    <div class="footer-col" style="left:500px"><h4>Quick Links</h4><ul><li>Home</li><li>Features</li><li>Pricing</li><li>Contact</li><li>Support</li></ul></div>
    <div class="footer-col" style="left:720px"><h4>Support</h4><ul><li>Privacy Policy</li><li>Terms &amp; Conditions</li><li>FAQs</li><li>Blog</li><li>Contact</li></ul></div>
    <div class="footer-col" style="left:944px"><h4>Follow Us</h4><ul><li>Pagebook</li><li>Snapgram</li><li>WorkLink</li><li>ViewTube</li></ul></div>
  </div>
  <div class="copyright">© Copyright 2026 | All Rights Reserved<span>Tidal Ledger</span></div>
</footer>

</body>
</html>
```